Webdesign für neue Weinmarke
Zielgruppe
Wolkenbrück ist eine neue Weinmarke. Es wird vorerst drei grundlegende Sorten geben: einen Rotwein, einen Weißwein und einen Rosé. Für diese neue Weinmarke wollen wir eine Webseite gestalten, welche die Weine ansprechend darstellt und zusätzlich den Kunden die Möglichkeit gibt, mehr Informationen über den Wein einzuholen. Die Marke Wolkenbrück ist auch im Etikett an den Graf von Tillenbrock angelehnt. Das Etikett zeigt den Baron, wie er auf einem Weinfass reitet – daher der Name „Wolkenbrück“. Die Story, die wir mit dem Wein spielen, ist, dass die besonderen Fähigkeiten des Barons auch auf den Genuss des Wolkenbrück zurückzuführen sind.
Die Zielgruppe für den Wolkenbrück ist breit gefächert und schließt per se erst mal keine Personengruppe aus. Der Wein soll eher im niedrigeren Preissegment verkauft werden.
Aufgabenstellung
Es soll eine neue Webseite designt werden, die sich im Aufbau an der die Webseite http://www.holvenbach.de/#!/de/unsere-weine/sortiment orientieren kann. Zudem können für die Entwicklung kleine Animationen berücksichtigt werden, die die Seite auflockern. Das Design soll eine responsive Webseite unterstützen. Das Design soll zur Weinmarke Wolkenbrück passen von der wir bisher nur das Etikett haben.

```html
<!DOCTYPE html>
<html lang="de">
<head>
<meta charset="utf-8">
<title>Wolkenbrück – Weine</title>
<link rel="stylesheet" href="https://fonts.googleapis.com/css2?family=Pathway+Gothic+One&family=Catamaran:wght@300;400;700&family=PT+Sans:wght@400&display=swap">
<style>
:root{
  --page:#e8e8e8;
  --white:#ffffff;
  --ink:#2b2b2b;
  --muted:#555555;
  --red:#7b1a20;
  --rose:#d9464b;
  --green:#8fb22f;
  --dark:#2a2624;
  --bar:#3b3533;
  --footer:#f3f3f3;
}
*{box-sizing:border-box;margin:0;padding:0}
html,body{width:1200px;height:3790px;overflow:hidden}
body{background:var(--page);font-family:"Catamaran",sans-serif;color:var(--ink);position:relative}
.page{position:absolute;left:40px;top:44px;width:1120px;height:3699px;background:var(--white)}
section{position:absolute;left:0;width:1120px;overflow:hidden}

/* Hero */
.hero{top:0;height:559px}
.hero-photo{position:absolute;inset:0;background:linear-gradient(100deg,#3b4a2c 0%,#6f7a45 30%,#9aa064 55%,#c9c08a 75%,#8f9a5a 100%)}
.hero-shade{position:absolute;inset:0}
.brand{position:absolute;left:62px;top:56px;font-family:"Pathway Gothic One",sans-serif;font-size:34px;letter-spacing:2px;color:var(--white)}
.menu{position:absolute;left:1025px;top:59px}
.knight{position:absolute;left:772px;top:88px;width:346px;height:457px;border-radius:40% 40% 30% 30%;background:radial-gradient(ellipse at center,rgba(60,55,45,.55),rgba(60,55,45,0) 70%)}
.hero-quote{position:absolute;left:62px;top:300px;font-family:"Pathway Gothic One",sans-serif;font-size:29px;line-height:33px;color:var(--white)}
.hero-text{position:absolute;left:62px;top:392px;width:600px;font-size:14px;line-height:22px;font-weight:300;color:var(--white)}
.dots{position:absolute;left:65px;top:478px;display:flex;gap:7px}
.dots span{width:20px;height:20px;border-radius:50%;background:rgba(255,255,255,.6)}
.dots span:first-child{background:var(--white)}

/* Products */
.product{height:553px}
.product .cell{position:absolute;top:0;width:560px;height:553px}
.cell.left{left:0}.cell.right{left:560px}
.bottle-stage{background:radial-gradient(ellipse at center,#ffffff 35%,#f1f1f1 100%)}
.bottle{position:absolute;left:232px;top:66px;width:96px;height:441px;border-radius:30px 30px 10px 10px}
.info{text-align:center}
.glass{position:absolute;left:260px;top:103px}
.info h2{position:absolute;left:0;width:560px;top:186px;font-family:"Pathway Gothic One",sans-serif;font-weight:400;font-size:40px;line-height:46px;color:var(--ink)}
.info h3{position:absolute;left:0;width:560px;top:238px;font-family:"PT Sans",sans-serif;font-weight:400;font-size:22px;line-height:28px}
.info p{position:absolute;left:55px;width:450px;top:309px;font-size:15px;line-height:19px;font-weight:300;color:#444}
.info a{position:absolute;left:0;width:560px;top:432px;font-size:15px;text-decoration:none}
.red h3,.red a{color:var(--red)}
.rose h3,.rose a{color:var(--rose)}
.white h3,.white a{color:var(--green)}

/* Region */
.region{top:2218px;height:559px}
.region-photo{position:absolute;inset:0;background:linear-gradient(180deg,#8a8a6a 0%,#7a7045 45%,#5b5226 75%,#3e3716 100%)}
.region h2{position:absolute;left:0;width:1120px;top:256px;text-align:center;font-family:"Pathway Gothic One",sans-serif;font-weight:400;font-size:36px;color:var(--white)}
.region-line{position:absolute;left:455px;top:306px}
.region p{position:absolute;font-size:17px;line-height:28px;font-weight:300;color:var(--white)}
.region p b{font-weight:700}
.region .east{left:620px;width:452px;top:128px;text-align:right}
.region .west{left:66px;width:500px;top:358px}

/* Story */
.story{top:2777px;height:488px}
.story-photo{position:absolute;inset:0;background:radial-gradient(ellipse at 50% 40%,#3e3834 0%,#2a2624 60%,#1c1917 100%)}
.story h2{position:absolute;left:0;width:1120px;top:68px;text-align:center;font-family:"Pathway Gothic One",sans-serif;font-weight:400;font-size:30px;color:var(--white)}
.story .col{position:absolute;top:168px;width:396px;font-size:12.5px;line-height:19.5px;font-weight:300;color:#e6e2de;text-align:justify;hyphens:auto}
.story .col.one{left:134px}.story .col.two{left:590px}
.arrow{position:absolute;top:242px}
.arrow.prev{left:46px}.arrow.next{left:1044px}

/* Footer */
.footer{top:3265px;height:382px;background:var(--footer);text-align:center}
.seal{position:absolute;left:483px;top:51px;width:132px;height:133px;border-radius:50%;background:radial-gradient(circle,#cfcfcf 0%,#e4e4e4 60%,rgba(243,243,243,0) 72%)}
.footer-name{position:absolute;left:0;width:1120px;top:198px;font-family:"Pathway Gothic One",sans-serif;font-size:28px;letter-spacing:2px;color:var(--ink)}
.footer-nav{position:absolute;left:0;width:1120px;top:254px;font-family:"PT Sans",sans-serif;font-size:17px;letter-spacing:1.5px;color:var(--muted)}
.footer-nav span{margin:0 10px}
.social{position:absolute;left:522px;top:310px;display:flex;gap:10px}
.social .square{width:32px;height:32px;background:#1f1f1f;border-radius:3px}
.bottom-bar{top:3647px;height:52px;background:var(--bar);color:#ddd;text-align:center;font-family:"PT Sans",sans-serif;font-size:15px;line-height:52px}
</style>
</head>
<body>
<div class="page">

  <section class="hero">
    <div class="hero-photo" role="img" aria-label="Foto: Weinreben mit blauen Trauben im Sonnenlicht"></div>
    <svg class="hero-shade" width="1120" height="559" viewBox="0 0 1120 559" aria-hidden="true">
      <polygon points="0,0 401,0 732,559 0,559" fill="rgba(40,35,30,0.42)"/>
    </svg>
    <div class="knight" role="img" aria-label="Illustration: der Graf reitet auf einem Weinfass, begleitet von Schwalben"></div>
    <div class="brand">WOLKENBRÜCK</div>
    <svg class="menu" width="44" height="38" viewBox="0 0 44 38" aria-label="Menü">
      <rect x="0" y="0" width="44" height="6" fill="#fff"/>
      <rect x="0" y="16" width="44" height="6" fill="#fff"/>
      <rect x="0" y="32" width="44" height="6" fill="#fff"/>
    </svg>
    <div class="hero-quote">“Der Wein, der schon dem Grafen<br>selbst Anmut und Heldengeist verlieh.”</div>
    <p class="hero-text">Genießen Sie Wolkenbrück als gehaltvollen und fruchtbetonten Rotwein, als lieblichen und fruchtigen Rosé oder als feinherben Riesling. Die drei Weine überzeugen durch höchste Qualität, harmonische Säuren und ein außergewöhnliches Design.</p>
    <div class="dots"><span></span><span></span></div>
  </section>

  <section class="product red" style="top:559px">
    <div class="cell left bottle-stage">
      <div class="bottle" role="img" aria-label="Produktfoto: Flasche Dornfelder halbtrocken" style="background:linear-gradient(90deg,#1e1518,#3a2430 50%,#1e1518)"></div>
    </div>
    <div class="cell right info">
      <svg class="glass" width="40" height="66" viewBox="0 0 40 66" aria-hidden="true">
        <path d="M4 2H36V18Q36 38 20 40Q4 38 4 18Z" fill="none" stroke="#7b1a20" stroke-width="4"/>
        <path d="M6 16H34Q33 36 20 37Q7 36 6 16Z" fill="#7b1a20"/>
        <rect x="18" y="40" width="4" height="18" fill="#7b1a20"/>
        <rect x="8" y="58" width="24" height="5" rx="2" fill="#7b1a20"/>
      </svg>
      <h2>Wolkenbrück Rotwein</h2>
      <h3>Des Wolkenbrücks Pfälzer Dornfelder</h3>
      <p>Des Wolkenbrücks Pfälzer Dornfelder, ein edler Tropfen, vermag es seinem Genießer wundersame Eindrücke zu verleihen. Rubinrot, fruchtbetont und gehaltvoll ermutigte er bereits den Grafen selbst, auf einem Weinfass über den Fluss zu reiten und trockenen Fußes am anderen Ufer anzukommen.</p>
      <a href="#">Zum Produkt</a>
    </div>
  </section>

  <section class="product rose" style="top:1112px">
    <div class="cell left info">
      <svg class="glass" width="40" height="66" viewBox="0 0 40 66" aria-hidden="true">
        <path d="M4 2H36V18Q36 38 20 40Q4 38 4 18Z" fill="none" stroke="#d9464b" stroke-width="4"/>
        <path d="M6 16H34Q33 36 20 37Q7 36 6 16Z" fill="#d9464b"/>
        <rect x="18" y="40" width="4" height="18" fill="#d9464b"/>
        <rect x="8" y="58" width="24" height="5" rx="2" fill="#d9464b"/>
      </svg>
      <h2>Wolkenbrück Rosé</h2>
      <h3>Des Wolkenbrücks lieblicher Rosé</h3>
      <p>Des Wolkenbrücks Pfälzer Dornfelder, ein edler Tropfen, vermag es seinem Genießer wundersame Eindrücke zu verleihen. Rubinrot, fruchtbetont und gehaltvoll ermutigte er bereits den Grafen selbst, auf einem Weinfass über den Fluss zu reiten und trockenen Fußes am anderen Ufer anzukommen.</p>
      <a href="#">Zum Produkt</a>
    </div>
    <div class="cell right bottle-stage">
      <div class="bottle" role="img" aria-label="Produktfoto: Flasche Dornfelder Rosé" style="background:linear-gradient(90deg,#b8202e,#ee5a66 50%,#b8202e)"></div>
    </div>
  </section>

  <section class="product white" style="top:1665px">
    <div class="cell left bottle-stage">
      <div class="bottle" role="img" aria-label="Produktfoto: Flasche Riesling feinherb" style="background:linear-gradient(90deg,#8e8a3c,#cfc985 50%,#8e8a3c)"></div>
    </div>
    <div class="cell right info">
      <svg class="glass" width="40" height="66" viewBox="0 0 40 66" aria-hidden="true">
        <path d="M4 2H36V18Q36 38 20 40Q4 38 4 18Z" fill="none" stroke="#8fb22f" stroke-width="4"/>
        <path d="M6 16H34Q33 36 20 37Q7 36 6 16Z" fill="#8fb22f"/>
        <rect x="18" y="40" width="4" height="18" fill="#8fb22f"/>
        <rect x="8" y="58" width="24" height="5" rx="2" fill="#8fb22f"/>
      </svg>
      <h2>Wolkenbrück Weißwein</h2>
      <h3>Des Wolkenbrücks Pfälzer Riesling</h3>
      <p>Des Wolkenbrücks Pfälzer Dornfelder, ein edler Tropfen, vermag es seinem Genießer wundersame Eindrücke zu verleihen. Rubinrot, fruchtbetont und gehaltvoll ermutigte er bereits den Grafen selbst, auf einem Weinfass über den Fluss zu reiten und trockenen Fußes am anderen Ufer anzukommen.</p>
      <a href="#">Zum Produkt</a>
    </div>
  </section>

  <section class="region">
    <div class="region-photo" role="img" aria-label="Foto: Weinberg mit Rebstöcken in der Abendsonne"></div>
    <svg style="position:absolute;inset:0" width="1120" height="559" viewBox="0 0 1120 559" aria-hidden="true">
      <polygon points="0,0 416,0 732,559 0,559" fill="rgba(168,62,52,0.55)"/>
      <polygon points="416,0 1120,0 1120,559 732,559" fill="rgba(110,150,90,0.35)"/>
    </svg>
    <h2>Regionalität</h2>
    <svg class="region-line" width="210" height="6" viewBox="0 0 210 6" aria-hidden="true"><rect x="0" y="2" width="210" height="2" fill="#fff"/></svg>
    <p class="east">Des Wolkenbrücks Rot- sowie Weißwein kommen aus dem <b>zweitgrößten deutschen Weinanbaugebiet, der Pfalz</b>. Das einzigartige Klima dieser Region bringt gehaltvolle und würzige Weine hervor. Die Pfalz ist Deutschlands größtes Rotweingebiet und beheimatet zudem auch des Wolkenbrücks feinherben Riesling.</p>
    <p class="west">Des Wolkenbrücks Rosé stammt aus <b>Rheinhessen – Deutschlands größtem Weinanbaugebiet</b>. Es zeichnet sich durch milde Durchschnittstemperaturen aus und lässt die Reben des leichten und lieblichen Rosés hervorragend heranreifen.</p>
  </section>

  <section class="story">
    <div class="story-photo" role="img" aria-label="Foto: dunkler Holztisch mit Weintrauben und Weinflasche"></div>
    <h2>Graf von Tillenbrock - Ritt auf dem Weinfass</h2>
    <p class="col one">Im Herbst jenes Jahres, als der Regen nicht enden wollte, stand der Graf von Tillenbrock am Ufer seines Weinbergs und sah, wie das Wasser den Keller des Gutes füllte. Die Fässer des neuen Jahrgangs schaukelten schon im Hof, und drüben im Dorf wartete man auf den Wein für das Lesefest. Die Fähre lag festgebunden, der Fährmann schlief, und kein Knecht wagte sich in die trübe Strömung. Der Graf aber band seinen Hut fest, prüfte den Spund des größten Fasses und schwang sich, als wäre es ein gesatteltes Pferd, auf dessen Rücken. Mit einer langen Rebstange lenkte er das Fass durch Wirbel und Strudel, grüßte die erstaunten Reiher am Schilf</p>
    <p class="col two">und sang dabei so laut, dass man ihn bis zur Kirche hörte. Einmal drehte sich das Fass dreimal um sich selbst, doch der Graf hielt sich mit Knien und Stange und lachte nur. Als er endlich am anderen Ufer anlegte, liefen ihm die Leute entgegen, halb voller Sorge, halb voller Neugier. Der Graf stieg trocken und heiter ab, klopfte dem Fass auf den Bauch und ließ es vor dem Gasthaus aufstellen. Man zapfte an, füllte die Becher und stieß auf die kühne Fahrt an. Bis tief in die Nacht erzählte der Graf von Strömung, Reihern und Regen, und jeder, der vom Wein kostete, schwor hernach, er habe selten einen gehaltvolleren Tropfen im Glas gehabt.</p>
    <svg class="arrow prev" width="30" height="42" viewBox="0 0 30 42" aria-label="Zurück"><polyline points="24,4 8,21 24,38" fill="none" stroke="#fff" stroke-width="7"/></svg>
    <svg class="arrow next" width="30" height="42" viewBox="0 0 30 42" aria-label="Weiter"><polyline points="6,4 22,21 6,38" fill="none" stroke="#fff" stroke-width="7"/></svg>
  </section>

  <section class="footer">
    <div class="seal" role="img" aria-label="Illustration: der Graf auf dem Weinfass in Grautönen"></div>
    <div class="footer-name">WOLKENBRÜCK</div>
    <nav class="footer-nav">HOME<span>I</span>KONTAKT<span>I</span>IMPRESSUM<span>I</span>DATENSCHUTZ</nav>
    <div class="social">
      <svg width="32" height="32" viewBox="0 0 32 32" aria-label="E-Mail">
        <rect x="1" y="1" width="30" height="30" rx="3" fill="#1f1f1f"/>
        <rect x="6" y="9" width="20" height="14" fill="none" stroke="#f3f3f3" stroke-width="2.5"/>
        <polyline points="6,9 16,17 26,9" fill="none" stroke="#f3f3f3" stroke-width="2.5"/>
      </svg>
      <div class="square" aria-label="Soziales Netzwerk"></div>
    </div>
  </section>

  <section class="bottom-bar">© 2018 Helm Getränke GmbH</section>
</div>
</body>
</html>
```